この度はまことにありがとうございます。
広告代理店です。

のぼりデザインのアイデアを頂戴できればと思っております。

入れる文字は下記になります。
梅 の さ と ・ ひ な た べ

ご不明な点などございましたらお気兼ねなくご連絡ください。
何卒、宜しくお願い申し上げます。
サイズの記載がございませんでした。

1800mm縦
600mmよこ

ロゴを縦組みいただいてもかまいません。

何卒、よろしくお願いします。
皆様のご提案に心より感謝申し上げます。

追記
目的をあらためてお知らせします。

このロゴだと背景色が白になりがちです。
しかしながらのぼりを外で使用する場合、背景に色を使わないと目立たないように感じます。

ロゴのイメージを崩さず少し目立つ(目立ちすぎなくて結構です。)のぼりが作れるかを
ご提案いただきたいのが今回の趣旨でございます。

もう1点は洋食っぽい?欧米風?の雰囲気といいますかおしゃれな感じを希望しています。
おしゃれさはかなりのポイントです。

結果的に背景白になるかもですが、、、。
背景が白がNGというわけではなくポイントでどう色を使うかです。

何卒、宜しくお願い申し上げます。

イメージに合うとても素敵なデザインでした。

この度はまことにありがとうございます。
皆様のご提案に心より感謝申し上げます。
また機会がございましたらよろしくお願い申し上げます。

```html
<!DOCTYPE html>
<html lang="ja">
<head>
<meta charset="utf-8">
<title>梅のさと・ひなたべ のぼり提案</title>
<link href="https://fonts.googleapis.com/css2?family=Kiwi+Maru:wght@400;500&family=Noto+Sans+JP:wght@400&display=swap" rel="stylesheet">
<style>
  :root {
    --paper: #ffffff;
    --green: #2f9a3c;
    --brown: #7b4a27;
    --title-brown: #8b5b3a;
    --tan: #b89c8b;
    --pole: #c9c9c9;
    --frame: #cfcfcf;
    --ink: #333333;
  }
  html, body {
    margin: 0;
    padding: 0;
    width: 847px;
    height: 1200px;
    overflow: hidden;
    background: var(--paper);
  }
  .sheet {
    position: relative;
    width: 847px;
    height: 1200px;
  }
  .sheet-caption {
    position: absolute;
    top: 26px;
    right: 20px;
    margin: 0;
    font: 400 10px/1 "Noto Sans JP", sans-serif;
    color: var(--ink);
    white-space: nowrap;
  }
  .flag-main {
    position: absolute;
    left: 119px;
    top: 113px;
    width: 328px;
    height: 984px;
    outline: 1px solid var(--frame);
  }
  .flag-mockup {
    position: absolute;
    left: 520px;
    top: 80px;
    width: 220px;
    height: 680px;
  }
  .flag-title {
    font-family: "Kiwi Maru", sans-serif;
    font-weight: 500;
    fill: var(--title-brown);
  }
  .flag-roman {
    font-family: "Kiwi Maru", sans-serif;
    fill: var(--paper);
  }
</style>
</head>
<body>
<main class="sheet">
  <p class="sheet-caption">■　梅のさと・ひなたべのぼり提案　サイズ縦1800mm×横600mm</p>

  <svg width="0" height="0" style="position:absolute" aria-hidden="true">
    <defs>
      <symbol id="nobori" viewBox="0 0 600 1800">
        <rect class="flag-ground" width="600" height="1800" fill="var(--paper)"/>
        <!-- top band -->
        <path class="band-brown" d="M0 0 H600 V60 C420 70 160 140 0 250 Z" fill="var(--brown)"/>
        <path class="band-green" d="M0 0 H600 V30 C420 40 150 100 0 200 Z" fill="var(--green)"/>
        <!-- bottom band -->
        <path class="band-brown" d="M0 1540 C180 1640 420 1600 600 1560 V1800 H0 Z" fill="var(--brown)"/>
        <path class="band-green" d="M0 1580 C180 1700 420 1740 600 1770 V1800 H0 Z" fill="var(--green)"/>
        <!-- roman name tag -->
        <rect class="roman-tag" x="250" y="185" width="62" height="420" fill="var(--tan)"/>
        <text class="flag-roman" x="281" y="205" font-size="30" style="writing-mode: vertical-rl" letter-spacing="2">ume no sato hinatabe</text>
        <!-- title -->
        <text class="flag-title" x="160" y="220" font-size="112" style="writing-mode: vertical-rl" letter-spacing="4">梅のさと・ひなたべ</text>
        <!-- illustration area -->
        <rect class="illustration" x="90" y="1260" width="420" height="160" rx="30" fill="#d9c7a0" role="img" aria-label="梅の枝と小鳥が並ぶイラスト"/>
      </symbol>
    </defs>
  </svg>

  <svg class="flag-main" viewBox="0 0 600 1800" role="img" aria-label="のぼりデザイン 梅のさと・ひなたべ">
    <use href="#nobori"/>
  </svg>

  <svg class="flag-mockup" viewBox="0 0 220 680" role="img" aria-label="ポールに付けたのぼりのイメージ">
    <rect class="pole" x="30" y="0" width="6" height="670" fill="var(--pole)"/>
    <rect class="pole-arm" x="30" y="52" width="176" height="4" fill="var(--pole)"/>
    <g class="pole-rings" fill="none" stroke="var(--pole)" stroke-width="2">
      <rect x="34" y="120" width="6" height="10"/>
      <rect x="34" y="260" width="6" height="10"/>
      <rect x="34" y="400" width="6" height="10"/>
      <rect x="34" y="540" width="6" height="10"/>
    </g>
    <svg x="40" y="60" width="164" height="492" viewBox="0 0 600 1800">
      <use href="#nobori"/>
    </svg>
  </svg>
</main>
</body>
</html>
```